依頼詳細
【依頼詳細】
業務用のラーメン専用出汁の外箱パッケージデザインを(箱デザイン)を依頼させていただます。
今回の依頼は本契約前にサンプルでお試し頂くためのパッケージとなりますので、初めて弊社商品と対面し、デザイン面から「驚き」の印象を与えたいと考えています。

また、今までは無地ダンボールで送っていたのですが、今回サイトのリニューアルに伴いパッケージにもデザイン変更を加えようと考えています。
サイトのリニューアルデザイン(添付資料参照)は、『イタリア感』をイメージした明るい配色のサイトにしています。
そのためパッケージデザインもこのような派手な配色でお願いできればと考えています。

同封される商品は別途添付(依頼書2.pdf)に記載しております。

【デザインの要望】
1、弊社は業界の中でも特に高額の高級商品であはありますが、あまり気取りすぎないデザインにしたいと考えています。
2、従来の食品業界でのデザインイメージを払拭するようなデザインをお願いします。今まで食品では見たことがないような配色と雰囲気を持たせたいです。(例えば原宿系POPデザインなど)
3、お客様が初めて弊社商品と対面する際に、「強く印象に残るデザイン」を重視して選考します。
4、色の指定はございません。皆様のセンスにお任せします。

【デザインに入れて欲しい内容】
・天然出汁【鶏】REGULAR SAMPLE

上記内容のみどこかに入れてください。小さくても構いません。
会社ロゴなどは入れても入れなくても構いません。

【参考デザイン】
tesslyの生理用品パッケージ
https://www.gettessly.co/products/box-builder

これくらい派手な色使いのデザインでも面白いかなと考えています。
記載項目
箱型パッケージデザインをお願いします。
【サイズ】横 350mm × 縦 200mm × 高さ 40mm

※詳細は添付イメージをご覧ください。
希望イメージ
シンプル 複雑
単色 カラフル
暗い 明るい
日常 高級
遊び心 厳粛
未来的 伝統的
女性的 男性的
希望する色
黄・オレンジ系
納品ファイル
• イラストレーター形式 (.ai)
• フォトショップ形式 (.psd)
補足説明
【添付ファイル内容】
・パッケージ外観イメージ
・リニューアルサイトイメージ(まだ仮組み中)
・弊社新ロゴサンプル画像
■ 選んだ理由

インパクトのある今までにはなかったデザインでした

■ 提案者全員のお礼・コメント

みなさまたくさんのご提案ありがとうございました。
どれも出来が良く、とても迷いました。また、近々似たようなコンペを開催させていただくかもしれませんが、その際はまたよろしくお願いします。

```html
<!DOCTYPE html>
<html lang="ja">
<head>
<meta charset="utf-8">
<title>天然出汁 鶏 REGULAR SAMPLE</title>
<link href="https://fonts.googleapis.com/css2?family=Yuji+Syuku&family=Oswald:wght@700&display=swap" rel="stylesheet">
<style>
  :root {
    --mustard-light: #d9a73a;
    --mustard: #c38f22;
    --mustard-deep: #a8731a;
    --ink-brown: #5e3e1c;
    --bowl-brown: #5a3718;
    --chili-red: #e8141b;
    --paper-white: #ffffff;
  }
  html, body {
    margin: 0;
    padding: 0;
    width: 1200px;
    height: 2400px;
    overflow: hidden;
    background: var(--chili-red);
  }
  .package {
    position: relative;
    width: 1200px;
    height: 2400px;
    overflow: hidden;
  }
  .upper-panel {
    position: absolute;
    left: 0;
    top: 0;
    width: 1200px;
    height: 1380px;
    background:
      radial-gradient(ellipse at 50% 35%, var(--mustard-light) 0%, var(--mustard) 55%, var(--mustard-deep) 100%);
  }
  .product-title {
    position: absolute;
    left: 50%;
    top: 150px;
    transform: translateX(-50%);
    margin: 0;
    writing-mode: vertical-rl;
    font-family: "Yuji Syuku", serif;
    font-weight: 400;
    font-size: 215px;
    line-height: 1;
    letter-spacing: 10px;
    color: var(--ink-brown);
  }
  .sample-bowl {
    position: absolute;
    left: 340px;
    top: 1068px;
    width: 520px;
    height: 312px;
  }
  .sample-label {
    position: absolute;
    left: 0;
    top: 1112px;
    width: 1200px;
    text-align: center;
    font-family: "Oswald", sans-serif;
    font-weight: 700;
    color: var(--paper-white);
    line-height: 1;
  }
  .sample-label .grade {
    display: block;
    font-size: 46px;
    letter-spacing: 1px;
  }
  .sample-label .kind {
    display: block;
    font-size: 62px;
    letter-spacing: 1px;
    margin-top: 10px;
  }
  .lower-panel {
    position: absolute;
    left: 0;
    top: 1380px;
    width: 1200px;
    height: 1020px;
    background: var(--chili-red);
  }
  .flavour-mark {
    position: absolute;
    left: 0;
    top: 70px;
    width: 1200px;
    margin: 0;
    text-align: center;
    font-family: "Yuji Syuku", serif;
    font-weight: 400;
    font-size: 860px;
    line-height: 1;
    color: var(--paper-white);
  }
</style>
</head>
<body>
  <main class="package">
    <section class="upper-panel" role="img" aria-label="Speckled mustard-yellow paper texture background">
      <h1 class="product-title">天然出汁</h1>
    </section>

    <svg class="sample-bowl" viewBox="0 0 520 312" aria-hidden="true">
      <path d="M0 0 H520 L400 210 H360 L365 312 H155 L160 210 H120 Z" fill="var(--bowl-brown)"/>
    </svg>
    <p class="sample-label">
      <span class="grade">REGULAR</span>
      <span class="kind">SAMPLE</span>
    </p>

    <section class="lower-panel">
      <h2 class="flavour-mark">鶏</h2>
    </section>
  </main>
</body>
</html>
```